Pilates business needs a face list flyer

We are a pilates business that has been based in England for 15 years and looking for a new flyer that is eye catch and modern but stylish
we are trying to capture the male market as well as the female market so the leaflet should draw attention to both groups.
I have attached a copy of the literature needed on the flyer also a picture of its founder

Target Market(s)

market age group 18-70+ male and female

Industry/Entity Type

Business

Font styles to use
Other font styles liked:
• calbri

Colors
33b8a4
34a7d8
3277b5
abd037

Requirements
Must have
• Literature attached
Nice to have
• To target both the male and female market. stylish but eye catching
Should not have
• pinks purples

```html
<!DOCTYPE html>
<html lang="en">
<head>
<meta charset="utf-8">
<title>Midshire Pilates – Tri-fold Flyer</title>
<link href="https://fonts.googleapis.com/css2?family=Oswald:wght@300;400&family=Open+Sans:wght@400;600;700&display=swap" rel="stylesheet">
<style>
:root{
  --teal:#33b8a4;
  --sky:#34a7d8;
  --blue:#3277b5;
  --navy:#1f4f93;
  --lime:#abd037;
  --ink:#3a3a3a;
  --paper:#ffffff;
  --fold:#f1f1f1;
  --bg:#e4e6e8;
}
*{margin:0;padding:0;box-sizing:border-box}
html,body{width:848px;height:1200px;overflow:hidden;background:var(--bg)}
body{position:relative;font-family:"Open Sans",Arial,sans-serif;color:var(--ink)}
.sheet{position:absolute;left:24px;width:800px;height:560px;background:var(--paper);overflow:hidden;box-shadow:0 2px 8px rgba(0,0,0,.18)}
.sheet--outside{top:20px}
.sheet--inside{top:620px}
.panel{position:absolute;top:0;height:100%}
.panel--a{left:0;width:262px}
.panel--b{left:262px;width:254px;background:linear-gradient(90deg,#f4f4f4,#fff 12%)}
.panel--c{left:516px;width:284px;background:linear-gradient(90deg,#f1f1f1,#fff 12%)}
.waves{position:absolute;left:0;width:800px;pointer-events:none}
.photo{position:absolute}
.heading{font-family:"Oswald",Arial,sans-serif;font-weight:300;color:var(--blue);text-transform:uppercase;letter-spacing:.2px}
.subheading{font-weight:700;color:var(--navy);font-size:12.5px;margin:9px 0 4px}
.body{font-size:7.6px;line-height:1.38;text-align:justify}
/* schedule */
.schedule{position:absolute;left:10px;top:18px;width:242px;text-align:center}
.schedule__item{margin-bottom:6.6px}
.schedule__time{font-size:9.4px;font-weight:700;color:var(--blue);line-height:1.2}
.schedule__venue{font-size:8.2px;line-height:1.2}
.circle{position:absolute;border-radius:50%;border:4px solid var(--navy)}
/* about */
.about{position:absolute;left:14px;top:24px;width:226px}
.about__title{font-size:15px;display:flex;align-items:center;gap:8px}
.about__title::after{content:"";flex:1;height:3px;background:var(--blue)}
.about__portrait{float:left;width:80px;height:80px;margin:10px 8px 4px 0}
.about .body{margin-top:8px}
.about .body + .body{margin-top:6px}
.contact{position:absolute;left:0;width:254px;text-align:center}
.contact__phone{font-family:"Oswald",Arial,sans-serif;font-weight:300;color:var(--blue);font-size:23px;top:400px}
.contact__line{font-size:10px;letter-spacing:.2px}
.social{position:absolute;left:14px;top:530px;color:#fff;font-size:8px;font-weight:600;display:flex;gap:6px;align-items:center}
/* brand */
.brand{position:absolute;left:0;width:284px;top:30px;text-align:center}
.brand__mark{width:58px;height:58px;background:var(--blue);margin:0 auto 12px}
.brand__name{font-family:"Oswald",Arial,sans-serif;font-weight:300;font-size:20px;color:var(--ink);text-transform:uppercase}
/* inside */
.banner{position:absolute;left:262px;top:0;width:538px;height:150px;background:linear-gradient(90deg,var(--teal),#2aa59a 60%,#3bb8a8)}
.banner__text{position:absolute;left:0;top:28px;width:230px;text-align:center;color:#fff}
.banner__name{font-size:12px;letter-spacing:.5px;text-transform:uppercase}
.banner__phone{font-family:"Oswald",Arial,sans-serif;font-weight:300;font-size:22px;margin-top:2px}
.col{position:absolute}
.col--a{left:22px;top:196px;width:226px}
.col--b{left:278px;top:196px;width:226px}
.col--c{left:534px;top:196px;width:250px}
.col .heading{font-size:18px;margin-bottom:8px}
.col .subheading:first-child{margin-top:0}
.benefits{list-style:none;font-size:7.6px;line-height:1.4;margin-top:3px}
.benefits li{padding-left:9px;position:relative}
.benefits li::before{content:"";position:absolute;left:1px;top:4px;width:3.5px;height:3.5px;border-radius:50%;background:var(--blue)}
.web{position:absolute;left:262px;width:254px;top:534px;text-align:center;font-size:10px;letter-spacing:.2px}
</style>
</head>
<body>

<!-- Outside of the tri-fold -->
<section class="sheet sheet--outside">

  <div class="panel panel--a">
    <div class="schedule">
      <div class="schedule__item"><div class="schedule__time">Monday 10.30am Beginner-Improver</div><div class="schedule__venue">The Meeting Hall, Mill Lane, Ashbrook</div></div>
      <div class="schedule__item"><div class="schedule__time">Monday 11.30am Small group Class.</div><div class="schedule__venue">The Meeting Hall, Mill Lane, Ashbrook</div></div>
      <div class="schedule__item"><div class="schedule__time">Monday 6.45pm Progressive-Intermediate+</div><div class="schedule__venue">St Aldric School, The Greenway, Fenwick</div></div>
      <div class="schedule__item"><div class="schedule__time">Monday 7.45pm Beginner-Improver</div><div class="schedule__venue">St Aldric School, The Greenway, Fenwick</div></div>
      <div class="schedule__item"><div class="schedule__time">Tuesday 5.45pm Small group class</div><div class="schedule__venue">The Parish Rooms, Market Rd, Hollowell</div></div>
      <div class="schedule__item"><div class="schedule__time">Tuesday 6.45pm Beginner-Improver</div><div class="schedule__venue">The Parish Rooms, Market Rd, Hollowell</div></div>
      <div class="schedule__item"><div class="schedule__time">Wednesday 10am Progressive</div><div class="schedule__venue">The Parish Rooms, Market Rd, Hollowell</div></div>
      <div class="schedule__item"><div class="schedule__time">Wednesday 11am Beginners</div><div class="schedule__venue">The Parish Rooms, Market Rd, Hollowell</div></div>
      <div class="schedule__item"><div class="schedule__time">Wednesday 6.45pm<br>Beginner-Progressive Thornby,</div><div class="schedule__venue">Community Centre, Broad St, Thornby, Nr Welham</div></div>
      <div class="schedule__item"><div class="schedule__time">Thursday 10am Beginner-Progressive</div><div class="schedule__venue">Church Hall, High St, Fenwick</div></div>
      <div class="schedule__item"><div class="schedule__time">Thursday 6.30pm Progressive-</div><div class="schedule__venue">The Meeting Hall, Mill Lane, Ashbrook</div></div>
      <div class="schedule__item"><div class="schedule__time">Thursday 7.30pm Beginner-Progressive</div><div class="schedule__venue">The Meeting Hall, Mill Lane, Ashbrook</div></div>
    </div>
  </div>

  <div class="panel panel--b">
    <div class="about">
      <h2 class="heading about__title">About Marianne</h2>
      <div class="photo about__portrait" role="img" aria-label="Portrait photo of the founder, Marianne" style="position:static;background:linear-gradient(160deg,#d6d6d6,#8c8c8c)"></div>
      <p class="body" style="margin-top:10px">Marianne is one of the most experienced and a leading Pilates teacher in the Midlands. She has been studying and working within the fitness industry for 20 years. Since 1992 she has specialized in aerobics, dance and other studio-based classes.</p>
      <p class="body" style="clear:both">In 1999, Marianne received her first degree in Sport and Leisure from the University of Harlow Vale. In 2000 she became the studio aerobic and fitness programme co-ordinator for the largest sports centre in England.</p>
      <p class="body">2001 saw Marianne studying and completing a Diploma in Pilates with Daniel Marsh, London. In 2002, Marianne established Midshire Pilates which bases its teaching practice on a Pilates method combining up to date knowledge of exercise physiology and techniques; whilst retaining the authentic concept of the method's founder. For the past 10 years Marianne has taught Pilates locally, nationally and internationally.</p>
      <p class="body">Since 2006 Marianne has continued with her professional development and studied Osteopathy, Traditional Acupuncture at Kingsmead University and Tai Chi. This wealth of knowledge and comprehensive skill-base brings a unique richness to her classes and private sessions.</p>
    </div>
    <div class="contact contact__phone" style="top:398px">CALL: 07700 900183</div>
    <div class="contact contact__line" style="top:436px">hello@midshirepilates.co.uk</div>
    <div class="contact contact__line" style="top:452px">www.midshire-pilates.co.uk</div>
  </div>

  <div class="panel panel--c">
    <div class="photo" role="img" aria-label="Photo of a group of women stretching in a studio class" style="left:0;top:150px;width:284px;height:410px;background:linear-gradient(135deg,#f4f1ee 0%,#e2d6cc 40%,#b9aaa0 75%,#8f8a87 100%)"></div>
    <div class="brand">
      <div class="brand__mark"></div>
      <div class="brand__name">Midshire Pilates</div>
    </div>
  </div>

  <svg class="waves" style="top:0" width="800" height="560" viewBox="0 0 800 560" aria-hidden="true">
    <path d="M0 470 C150 440 280 455 420 480 C560 505 680 470 800 400 L800 560 L0 560 Z" fill="var(--teal)"/>
    <path d="M260 455 C380 470 500 500 620 490 C700 482 760 455 800 430 L800 455 C740 495 660 520 560 522 C460 524 360 500 260 470 Z" fill="var(--lime)"/>
    <path d="M330 490 C450 515 560 530 660 515 C720 505 770 480 800 460 L800 520 C740 545 640 555 540 548 C460 540 390 520 330 500 Z" fill="var(--navy)"/>
    <path d="M300 478 C420 500 540 520 650 505 C720 495 770 470 800 450 L800 458 C770 478 720 504 650 513 C540 528 420 508 300 486 Z" fill="#fff"/>
    <path d="M516 500 C610 470 700 420 800 340 L800 420 C720 465 630 500 516 512 Z" fill="var(--lime)"/>
  </svg>
  <div class="circle photo" role="img" aria-label="Photo of a woman in a plank on an exercise mat" style="left:22px;top:438px;width:108px;height:108px;background:linear-gradient(135deg,#f0e6de,#b99682)"></div>
  <div class="circle photo" role="img" aria-label="Photo of a class using resistance rings" style="left:132px;top:438px;width:100px;height:100px;background:linear-gradient(135deg,#e7e2de,#8d8c92)"></div>
  <div class="social" style="left:276px">LIKE US AT <span>Midshire Pilates</span></div>
</section>

<!-- Inside of the tri-fold -->
<section class="sheet sheet--inside">
  <div class="photo" role="img" aria-label="Photo of a woman doing a leg raise on a mat with a foam roller" style="left:0;top:0;width:262px;height:140px;background:linear-gradient(160deg,#ffffff 20%,#e9edf0 55%,#c7d2db)"></div>
  <div class="banner">
    <div class="banner__text">
      <div class="banner__name">Midshire Pilates</div>
      <div class="banner__phone">CALL: 07700 900183</div>
    </div>
  </div>
  <svg class="waves" style="top:80px" width="800" height="140" viewBox="0 0 800 140" aria-hidden="true">
    <path d="M0 55 C150 95 330 90 500 55 C620 30 720 35 800 45 L800 140 L0 140 Z" fill="#fff"/>
    <path d="M0 55 C150 95 330 90 500 55 C620 30 720 35 800 45 L800 62 C720 50 620 50 500 72 C330 105 150 105 0 70 Z" fill="var(--teal)"/>
    <path d="M262 82 C400 70 520 40 640 32 C720 28 770 35 800 42 L800 70 C740 58 660 55 560 70 C460 85 360 95 262 95 Z" fill="var(--navy)"/>
    <path d="M520 62 C620 48 720 55 800 70 L800 95 C720 80 620 78 520 72 Z" fill="var(--lime)"/>
    <path d="M0 70 C60 88 120 98 190 102 L190 106 C120 104 60 95 0 80 Z" fill="var(--teal)"/>
  </svg>

  <div class="col col--a">
    <h2 class="heading">What is Pilates?</h2>
    <p class="body">Pilates is now the hottest and most talked about fitness trend since the aerobic explosion of the past 30 years. A perfect blend of Eastern and Western philosophy. Pilates is a holistic approach to exercise, that integrates body and mind. It concentrates on building strength, stamina, balance and co-ordination, improving flexibility, coordination, posture, breathing and well-being.</p>
    <h3 class="subheading">Classes</h3>
    <p class="body">All classes are based upon the original 34 movements developed by the method's founder. Classes provide low impact yet highly intense workouts, ideal for everyone, whatever age or ability or whether the individual is fit, sedentary or recuperating after illness or surgery. Furthermore, Pilates provides a safe and beneficial workout for expectant and new mothers.</p>
    <p class="body" style="margin-top:6px">Each session is designed to,</p>
    <ul class="benefits">
      <li>change the way you look</li>
      <li>create lean muscles</li>
      <li>Increase strength, flexibility, coordination and proper body alignment</li>
      <li>Increase core strength</li>
      <li>Reduce fatigue, stress and risk of injury</li>
      <li>Reduce back and joint pain</li>
      <li>Rehabilitation</li>
      <li>Increase circulation</li>
      <li>Improve body mind integration</li>
    </ul>
  </div>

  <div class="col col--b">
    <h2 class="heading">Class Description</h2>
    <h3 class="subheading">Small Group Pilates (new)</h3>
    <p class="body">This class is structured similar to a private session. Max of 6 people allows movement plans to be more tailored to individual's needs than a larger group class. Will take from the basics and help to build on these skills to improve posture and to develop strength and flexibility. Home plan provided</p>
    <h3 class="subheading">Beginner-Improvers</h3>
    <p class="body">Ideal for those new to the Pilates technique. In this programme you will develop an understanding of the principals, gain strength, stamina and flexibility safely, as you are guided through a series of beginner movements, modified and tailored to your own needs and ability.</p>
    <h3 class="subheading">Beginner-Improvers</h3>
    <p class="body">Ideal stepping stone from beginners building on moves that you have already learnt at a more intense level, as well as learning new moves. Incorporating small equipment such as the isotoner, the stability ball, roller and Pilates balance weights to help increase the intensity of the workout without it being over challenging for those still developing their skill base.</p>
  </div>

  <div class="col col--c" style="top:186px">
    <h3 class="subheading" style="margin-top:0">Intermediate-Advanced</h3>
    <p class="body">This class is designed for those already well versed in the Pilates technique. Both physically and mentally challenging, new movements are incorporated with combinations and higher intensity of known movements, alongside with the use of small equipment</p>
    <h2 class="heading" style="margin-top:12px">Private Sessions</h2>
    <p class="body">Perfect for anyone with specific needs, restricted time frame, or limited ability. Sessions are built using the 8 Pilates principals and designed to encompass all your individual needs, with the focus upon restoring strength, flexibility, equilibrium and well being. Continued support and home movement plans are provided to help motivate and to help with achieving your goals.<br>Your private session can be arranged in the convenience of your own home or a location near to you. Please contact Marianne for further details and availability.</p>
  </div>

  <div class="photo" role="img" aria-label="Photo of women exercising on stability balls" style="left:516px;top:462px;width:284px;height:98px;border-radius:60px 0 0 0;border-top:4px solid var(--navy);background:linear-gradient(135deg,#efe7e1,#a9b4bd 60%,#6f7f8c)"></div>
  <div class="web">www.midshire-pilates.co.uk</div>
</section>

</body>
</html>
```